Steel Company / Iron Railing Business Card Template

We are a custom steel fabrication company located in Corvale, DE. In business since 1979, we recently developed a new logo, and we're looking for a business card design to help display the new logo and our business. The name of the company is Kelbrook Forge Co.. The Office Phone number is (610) 555-0143. We fabricate and install custom "wrought iron" railings on our residential side, we also fabricate and erect structural steel (think cranes and steel beams in buildings) on our commercial side. Looking to get a business card template designed. Something modern, but professional. Clear and easy to read. Front should have all business and employee information including phone number(s), email address, business information, etc. back should spotlight logo.

Industry/Entity Type

Construction / Home Improvement

Contact Information for Business Card

Business information is Kelbrook Forge Co., 48 Dunmore Ave Suite 3305, Corvale, DE 19074. Phone number is (610) 555-0143. Website is www.kelbrookforge.example Business card should be for "Tom Pelling" with the job title "Sales & Estimating" but be editable for other employees. Tom's phone number is (610) 555-0178

Colors

Designer to choose colors to be used in the design.

Requirements
Must have
• Modern Feel, Design should be sized for standard business card sizing 3.5" x 2" (88.9mm x 50.8mm)

```html
<!DOCTYPE html>
<html lang="en">
<head>
<meta charset="utf-8">
<title>Kelbrook Forge Co. Business Card</title>
<link href="https://fonts.googleapis.com/css2?family=Montserrat:wght@400;500;700&display=swap" rel="stylesheet">
<style>
  :root {
    --stage: #3a3a3c;
    --card: #1d1d1f;
    --blue: #2447a8;
    --red: #e0232e;
    --white: #f4f4f4;
    --emboss: #2a2a2c;
  }
  * { margin: 0; padding: 0; box-sizing: border-box; }
  html, body { width: 1200px; height: 875px; overflow: hidden; background: var(--stage); }
  body { font-family: "Montserrat", sans-serif; position: relative; }

  .card {
    position: absolute;
    left: 285px;
    width: 630px;
    height: 360px;
    border-radius: 22px;
    background: var(--card);
    overflow: hidden;
    box-shadow: 0 14px 30px rgba(0,0,0,.45);
  }
  .card--back { top: 50px; }
  .card--front { top: 465px; }

  /* Back */
  .back-brand {
    position: absolute; inset: 0;
    display: flex; align-items: center; justify-content: center; gap: 16px;
  }
  .back-brand__dot { width: 28px; height: 28px; border-radius: 50%; background: var(--emboss); }
  .back-brand__name { font-weight: 700; font-size: 40px; color: var(--emboss); letter-spacing: .5px; }

  /* Front */
  .front-wave { position: absolute; inset: 0; }
  .front-tab {
    position: absolute; left: 0; top: 88px;
    width: 14px; height: 48px; background: var(--blue);
    border-radius: 0 6px 6px 0;
  }
  .contact { position: absolute; left: 40px; top: 74px; color: var(--white); }
  .contact__name { font-weight: 700; font-size: 28px; letter-spacing: .5px; line-height: 1; }
  .contact__first { color: var(--blue); }
  .contact__last { color: var(--red); }
  .contact__title { font-size: 16px; margin-top: 8px; }
  .contact__line { display: flex; align-items: center; gap: 9px; font-size: 15px; margin-top: 6px; }
  .contact__address { font-size: 15px; line-height: 1.35; margin-top: 18px; padding-left: 24px; }
  .contact__group { margin-top: 16px; }
  .icon { width: 15px; height: 15px; flex: none; }

  .front-brand {
    position: absolute; right: 40px; top: 40px;
    display: flex; align-items: center; gap: 12px;
  }
  .front-brand__dot { width: 22px; height: 22px; border-radius: 50%; background: var(--red); }
  .front-brand__name { font-weight: 700; font-size: 27px; color: var(--blue); line-height: 1.1; }
</style>
</head>
<body>

<section class="card card--back" aria-label="Card back">
  <div class="back-brand">
    <span class="back-brand__dot"></span>
    <span class="back-brand__name">Kelbrook Forge Co.</span>
  </div>
</section>

<section class="card card--front" aria-label="Card front">
  <svg class="front-wave" viewBox="0 0 630 360" preserveAspectRatio="none" aria-hidden="true">
    <path d="M160 360 C 330 345, 440 270, 505 200 C 545 160, 590 145, 630 140 L630 360 Z" fill="var(--red)"/>
    <path d="M190 360 C 350 350, 450 285, 515 215 C 555 175, 595 160, 630 157 L630 360 Z" fill="var(--blue)"/>
  </svg>
  <div class="front-tab"></div>

  <div class="contact">
    <div class="contact__name"><span class="contact__first">TOM</span> <span class="contact__last">PELLING</span></div>
    <div class="contact__title">Sales &amp; Estimating</div>
    <div class="contact__line">
      <svg class="icon" viewBox="0 0 16 16"><rect x="4" y="1" width="8" height="14" rx="1.5" fill="none" stroke="var(--red)" stroke-width="1.6"/><circle cx="8" cy="12.5" r="0.9" fill="var(--red)"/></svg>
      (610) 555-0178
    </div>
    <div class="contact__address">48 Dunmore Ave Suite 3305<br>Corvale, DE 19074</div>
    <div class="contact__group">
      <div class="contact__line">
        <svg class="icon" viewBox="0 0 16 16"><path d="M3 2l3 0 1 3.5-2 1.3c.9 1.9 2.3 3.3 4.2 4.2l1.3-2 3.5 1v3c0 .6-.5 1-1 1C7 14 2 9 2 3c0-.5.4-1 1-1z" fill="var(--red)"/></svg>
        (610) 555-0143
      </div>
      <div class="contact__line">
        <svg class="icon" viewBox="0 0 16 16"><rect x="1" y="3" width="14" height="10" rx="1" fill="var(--red)"/><path d="M1.5 3.5L8 9l6.5-5.5" fill="none" stroke="var(--card)" stroke-width="1.3"/></svg>
        info@kelbrookforge.example
      </div>
      <div class="contact__line">
        <svg class="icon" viewBox="0 0 16 16" fill="none" stroke="var(--red)" stroke-width="1.3"><circle cx="8" cy="8" r="6.5"/><ellipse cx="8" cy="8" rx="3" ry="6.5"/><path d="M1.5 8h13M2.5 5h11M2.5 11h11"/></svg>
        www.kelbrookforge.example
      </div>
    </div>
  </div>

  <div class="front-brand">
    <span class="front-brand__dot"></span>
    <span class="front-brand__name">Kelbrook<br>Forge Co.</span>
  </div>
</section>

</body>
</html>
```